Coffee Brand Poster Ad

We' re looking for design of poster advertisement for our coffee brand, kind of poster we can put in elevators or buses (approx. size 50x60cm), so we're looking for something original and eye-catchy ideas. We dont have our own specific slogan for this, so feel free to experiment. It is high-quality instant coffee made according to european nordic recipe, our target are women in overall, but mainly young, middle-class modern girls. It is high-quality instant coffee made according to european nordic recipe. Were trying to turn drinking coffee into lifestyle choice for young chinese girls by emphasizing western influence for our brand, also focus on elegance and classy style in packaging and advertisements. Our coffee brand is currently dedicated to sell mainly in China so we prefer english and chinese simplified version. If youre not familiar with chinese language you can use online translator, we will correct or adjust it to our needs.

Target Market(s)

Industry/Entity Type

Requirements
Must have
• - Our brand logo (*cdr and *png file included as attachement)
- Poster size 50x60 cm
- Originality and creative idea
Nice to have
• - Should draw attention and create curiosity at first sight
- It should emphasize 'CLASSY' style of our coffee or lifestyle of young energetic girls
- might compare chinese and western lifestyle
Should not have
• - Don't try to focus on "waking up" aspect of coffee
- Too much coffe beans

```html
<!DOCTYPE html>
<html lang="en">
<head>
<meta charset="utf-8">
<title>Fjord Roast – Instant Coffee Poster</title>
<link rel="stylesheet" href="https://fonts.googleapis.com/css2?family=Bodoni+Moda:wght@400;500&display=swap">
<style>
  :root {
    --page: #ffffff;
    --band-light: #8a8682;
    --band-dark: #45413e;
    --cream-light: #f3ece4;
    --cream-dark: #e9dfd4;
    --headline-grey: #a9a5a1;
    --headline-white: #f7f4f0;
    --brand-brown: #5a3a2a;
    --label-card: #f8f3ec;
  }
  html, body {
    margin: 0;
    padding: 0;
    width: 1108px;
    height: 1200px;
    overflow: hidden;
    background: var(--page);
  }
  .canvas {
    position: relative;
    width: 1108px;
    height: 1200px;
  }
  .poster {
    position: absolute;
    left: 325px;
    top: 325px;
    width: 450px;
    height: 541px;
  }
  .poster svg { display: block; }
  .headline-text { font-family: "Bodoni Moda", serif; }
</style>
</head>
<body>
<div class="canvas">
  <div class="poster">
    <svg width="450" height="541" viewBox="0 0 450 541" xmlns="http://www.w3.org/2000/svg">
      <defs>
        <radialGradient id="bandGlow" cx="50%" cy="55%" r="70%">
          <stop offset="0%" stop-color="var(--band-light)"/>
          <stop offset="100%" stop-color="var(--band-dark)"/>
        </radialGradient>
        <linearGradient id="creamFade" x1="0" y1="0" x2="0" y2="1">
          <stop offset="0%" stop-color="var(--cream-dark)"/>
          <stop offset="100%" stop-color="var(--cream-light)"/>
        </linearGradient>
      </defs>

      <!-- headline band -->
      <rect class="headline-band" x="0" y="0" width="450" height="242" fill="url(#bandGlow)"/>
      <text class="headline-text" x="17" y="139" font-size="88" font-weight="400"
            fill="var(--headline-grey)" textLength="414" lengthAdjust="spacingAndGlyphs">ARE YOU</text>
      <text class="headline-text" x="18" y="169" font-size="27" font-weight="400"
            fill="none" stroke="var(--headline-white)" stroke-width="0.8"
            textLength="412" lengthAdjust="spacingAndGlyphs">CRAVING AN INSTANT HOT</text>
      <text class="headline-text" x="17" y="209" font-size="42" font-weight="500"
            fill="var(--headline-white)" textLength="414" lengthAdjust="spacingAndGlyphs">CUP OF COFFEE?</text>

      <!-- welcome area -->
      <rect class="welcome-area" x="0" y="242" width="450" height="299" fill="url(#creamFade)"/>
      <text class="headline-text" x="225" y="343" font-size="15" text-anchor="middle"
            fill="var(--brand-brown)" letter-spacing="1">WELCOME TO</text>

      <!-- brand card -->
      <rect class="brand-card" x="125" y="363" width="204" height="123" fill="var(--label-card)"/>
      <text class="headline-text" x="227" y="432" font-size="30" font-weight="400"
            text-anchor="middle" fill="var(--brand-brown)">Fjord Roast</text>
    </svg>
  </div>
</div>
</body>
</html>
```